New Branding Business Card Design

Redesign business card according to new branding update.

** The design received so far are single color + BLACK.
I'd encourage designer to use different tones of blue / purple as described in the Designer Brief color palette

Target Market(s)

International

Industry/Entity Type

Medical Equipment

Contact Information for Business Card

Logo on one side (Designer can decide if they want to move certain info from the other side to save space)

Main body info (company name, individual name in both English and Chinese, contact info etc) on the other
Prefer a 'cleaner' layout - vs 'all over the place'
Prefer flush left alignment

Font styles to use
Sans Serif

Requirements
Must have
• Key info
• (Company name (English)): VORAK (HK) Limited
• (Name (English)): Martin L. Osei
• (Credential): FCPA, FHKSI
• (Title): Founder, Managing Director & CEO
• For the following info, designers decide whether to use colon or no colon, stroke separator, or use icon gfx for T (for telephone fixed line, M for mobile etc.)
• T: +852 2741 VORAK / +852 2741 5317
• M: +852 9473 6215 / + 86 139 4527 3916
• E: martin.l.osei@vorak-example.hk
Nice to have
• Depending on the space and spacing available designers can add or use fuller title and other info
• Title: Chairman of the Executive Committee, Founder, Managing Director & CEO
• (Name (Chinese)): 梁文浩
Should not have
• One of our business entities a long company name that cannot be broken into 2 lines
• makes vertical implementation almost impossible

```html
<!DOCTYPE html>
<html lang="en">
<head>
<meta charset="utf-8">
<title>VORAK (HK) Limited — Business Card</title>
<link rel="stylesheet" href="https://fonts.googleapis.com/css2?family=Poppins:wght@400;500;600&family=Noto+Sans+TC:wght@400&display=swap">
<style>
  :root {
    --purple: #5a2a86;
    --purple-deep: #4b2173;
    --ink: #1c1c1c;
    --paper: #ffffff;
    --backdrop: #ece9ef;
  }
  * { margin: 0; padding: 0; box-sizing: border-box; }
  html, body { width: 1200px; height: 1040px; overflow: hidden; }
  body {
    background: var(--backdrop);
    font-family: "Poppins", sans-serif;
    position: relative;
  }
  .card {
    position: absolute;
    left: 180px;
    width: 840px;
    height: 480px;
    border-radius: 30px;
    overflow: hidden;
    box-shadow: 0 10px 28px rgba(40, 20, 60, 0.18);
  }
  .card--front { top: 26px; background: var(--paper); }
  .card--back { top: 534px; background: var(--purple); }

  .wordmark {
    position: absolute;
    display: flex;
    align-items: center;
    gap: 10px;
    font-weight: 600;
    letter-spacing: 2px;
  }
  .wordmark__square { display: block; border-radius: 4px; }
  .card--front .wordmark { top: 40px; right: 48px; color: var(--purple); font-size: 24px; }
  .card--front .wordmark__square { width: 22px; height: 22px; background: var(--purple); }
  .card--back .wordmark {
    top: 50%; left: 50%; transform: translate(-50%, -50%);
    color: var(--paper); font-size: 64px; gap: 20px; letter-spacing: 6px;
  }
  .card--back .wordmark__square { width: 56px; height: 56px; background: var(--paper); border-radius: 10px; }

  .identity { position: absolute; left: 68px; top: 168px; }
  .identity__chinese {
    font-family: "Noto Sans TC", sans-serif;
    color: var(--purple); font-size: 17px; line-height: 1;
  }
  .identity__name {
    color: var(--purple); font-size: 38px; font-weight: 500; line-height: 1.15; margin-top: 4px;
  }
  .identity__credential { font-size: 17px; font-weight: 500; margin-left: 4px; }
  .identity__title { color: var(--ink); font-size: 17px; line-height: 1.4; }

  .company { color: var(--purple); font-size: 18px; font-weight: 600; margin-top: 20px; }
  .contacts { list-style: none; margin-top: 4px; }
  .contacts li {
    display: flex; align-items: center; gap: 12px;
    color: var(--ink); font-size: 16px; line-height: 1.5;
  }
  .contacts svg { width: 14px; height: 14px; flex: none; }
  .contacts .sep { color: var(--purple); margin: 0 6px; }

  .accent-bar {
    position: absolute; left: 110px; bottom: 0;
    width: 160px; height: 9px; background: var(--purple);
    border-radius: 4px 4px 0 0;
  }
</style>
</head>
<body>
  <section class="card card--front" aria-label="Business card front">
    <div class="wordmark"><span class="wordmark__square"></span>VORAK</div>

    <div class="identity">
      <p class="identity__chinese">梁文浩</p>
      <h1 class="identity__name">Martin L. Osei<span class="identity__credential">FCPA, FHKSI</span></h1>
      <p class="identity__title">Chairman of the Executive Committee</p>
      <p class="identity__title">Founder, Managing Director &amp; CEO</p>

      <p class="company">VORAK (HK) Limited</p>
      <ul class="contacts">
        <li>
          <svg viewBox="0 0 16 16" aria-hidden="true"><path fill="#5a2a86" d="M3.5 1.5l2.4 2.6-1.3 1.8c.9 2 2.6 3.7 4.6 4.6l1.8-1.3 2.6 2.4-1.4 2.2C6.5 13.6 2.4 9.5 1.3 3z"/></svg>
          <span>+852 2741 VORAK<span class="sep">|</span>+852 2741 5317</span>
        </li>
        <li>
          <svg viewBox="0 0 16 16" aria-hidden="true"><rect x="3.5" y="1" width="9" height="14" rx="1.5" fill="none" stroke="#5a2a86" stroke-width="1.6"/><rect x="6.5" y="12" width="3" height="1.2" fill="#5a2a86"/></svg>
          <span>+852 9473 6215<span class="sep">|</span>+ 86 139 4527 3916</span>
        </li>
        <li>
          <svg viewBox="0 0 16 16" aria-hidden="true"><rect x="1" y="3" width="14" height="10" rx="1" fill="#5a2a86"/><path d="M1.5 3.8L8 9l6.5-5.2" fill="none" stroke="#fff" stroke-width="1.2"/></svg>
          <span>martin.l.osei@vorak-example.hk</span>
        </li>
      </ul>
    </div>

    <div class="accent-bar"></div>
  </section>

  <section class="card card--back" aria-label="Business card back">
    <div class="wordmark"><span class="wordmark__square"></span>VORAK</div>
  </section>
</body>
</html>
```